Lip Balm Label Design

Design a label for a Lavender-Mint lip balm. We make high-quality natural essential oil products. Please use the old label as an example of what exists. The label should include purple. The final design should be eye-catching and distinct. The file should be in an AI file.

Here is the information that should be included on the label:
1) ingredients:Theobroma Cacao (Cocoa) Seed Butter, Theobroma grandiflorum Ultra Refined Butter, beesewax, Calendula Officinalis Flower Oil, Prunus Amygdalus Dulcis (Sweet Almond) Oil, cetyl alcohol and Tocopherol. Lavandula Angustifolia (Lavender) Oil and Mentha Piperita (Peppermint) Oil.

2) www.kelvorascents.com

3) Brand name and logo: K. Velora Aromatherapy (logo is attached- you can use with form)

```html
<!DOCTYPE html>
<html lang="en">
<head>
<meta charset="utf-8">
<title>K. Velora Aromatherapy – Lavender-Mint Lip Balm Label</title>
<link href="https://fonts.googleapis.com/css2?family=Arimo:wght@400;700&display=swap" rel="stylesheet">
<style>
  :root {
    --page-bg: #e9e9ec;
    --label-purple: #8f66a9;
    --label-purple-deep: #825a9c;
    --band-purple: #6a4584;
    --pill-purple: #4f2f63;
    --ink-white: #ffffff;
    --ink-soft: #f3eef7;
  }
  * { margin: 0; padding: 0; box-sizing: border-box; }
  html, body {
    width: 1200px;
    height: 900px;
    overflow: hidden;
    background: var(--page-bg);
    font-family: "Arimo", Arial, sans-serif;
  }
  .label {
    position: absolute;
    left: 100px;
    top: 46px;
    width: 1000px;
    height: 808px;
    background: var(--label-purple);
    overflow: hidden;
  }
  .label__band {
    position: absolute;
    left: 0;
    width: 100%;
    height: 12px;
    background: var(--band-purple);
  }
  .label__band--top { top: 0; }
  .label__band--bottom { bottom: 0; }
  .label__sprig-art {
    position: absolute;
    left: 330px;
    top: 40px;
    width: 620px;
    height: 720px;
    background: radial-gradient(ellipse at center, var(--label-purple-deep) 0%, rgba(130, 90, 156, 0.4) 55%, rgba(143, 102, 169, 0) 75%);
  }
  .ingredients {
    position: absolute;
    left: 66px;
    top: 764px;
    width: 724px;
    transform: rotate(-90deg);
    transform-origin: top left;
    color: var(--ink-soft);
    font-size: 19.5px;
    line-height: 1.32;
    text-align: justify;
    letter-spacing: 0.2px;
  }
  .ingredients__heading { font-weight: 700; }
  .brand {
    position: absolute;
    left: 400px;
    top: 250px;
    width: 440px;
    text-align: center;
    color: var(--ink-white);
    font-weight: 400;
  }
  .brand__name {
    font-size: 78px;
    letter-spacing: 1px;
    line-height: 1;
  }
  .brand__tag {
    margin-top: 6px;
    font-size: 22px;
    letter-spacing: 2px;
    text-transform: uppercase;
  }
  .flavour {
    position: absolute;
    left: 384px;
    top: 488px;
    width: 470px;
    height: 74px;
    border-radius: 37px;
    background: var(--pill-purple);
    color: var(--ink-white);
    font-size: 40px;
    letter-spacing: 3px;
    line-height: 74px;
    text-align: center;
  }
  .website {
    position: absolute;
    left: 384px;
    top: 657px;
    width: 470px;
    text-align: center;
    color: var(--ink-white);
    font-size: 31px;
  }
  .website__domain { font-weight: 700; }
  .net-weight {
    position: absolute;
    left: 384px;
    top: 725px;
    width: 470px;
    text-align: center;
    color: var(--ink-white);
    font-size: 31px;
    font-weight: 700;
  }
</style>
</head>
<body>
  <section class="label" aria-label="Lavender-Mint lip balm label">
    <div class="label__band label__band--top"></div>
    <div class="label__sprig-art" role="img" aria-label="Faint lavender sprig line illustration behind the brand name"></div>

    <p class="ingredients">
      <span class="ingredients__heading">ingredients:</span>Theobroma Cacao (Cocoa) Seed Butter, Theobroma grandiflorum Ultra Refined Butter, beesewax, Calendula Officinalis Flower Oil, Prunus Amygdalus Dulcis (Sweet Almond) Oil, cetyl alcohol and Tocopherol. Lavandula Angustifolia (Lavender) Oil and Mentha Piperita (Peppermint) Oil.
    </p>

    <div class="brand">
      <div class="brand__name">K. Velora</div>
      <div class="brand__tag">Aromatherapy</div>
    </div>

    <div class="flavour">LAVENDER-MINT</div>

    <p class="website">www.<span class="website__domain">kelvorascents</span>.com</p>
    <p class="net-weight">0.15 oz (4.4 mls)</p>

    <div class="label__band label__band--bottom"></div>
  </section>
</body>
</html>
```